Recruitment company website redesign

We're looking to redesign our current website, located at http://www.crestwayhire.com.au, to make it more FRESH, modern, easy-to-navigate, and user-friendly. Navigation should be very obvious, and buttons should be big. The design should be closer to the flat/clean look of Zorvik or Qelt9 rather than the somewhat older embossed look.

The design also needs to take into consideration that the coding will be responsive (mobile, tablet, etc.-friendly).

We'd like to see your work on two pages, and from there, we'll choose a designer that we will pay further to design the rest of the site. The two pages we will need are:

1. A home page, with the content detailed in the attached image home-outline.jpg. Keep in mind that this is a very rough outline with no design whatsoever, so please take those elements and create a beautiful page from it. Feel free to move the content around if necessary, as long as that's all on there. We're pretty open to whatever you think would look best.

Using high quality images could look great, and we'd purchase the perfect stock photos down the line, but for now just use any business-related images that aren't too cheesy (stay away from anything that looks too stock image-y like smiling actors).

2. A talent dashboard. This will live as a separate microsite; therefore, the design should be consistent with the home page but also be separate. Here, you have some more freedom with the design, but use our overall style and make it look like a user dashboard - very simple and easy to translate for responsive design.

There should be a horizontal menu that includes: "Edit Profile," "Apply for a Job," "WHS" (this will have a drop-down submenu), "My History" (also with a drop-down submenu), and "Contact."

Above that menu should be a place for users to sign in/out. Below the menu will be a welcome message and then a notice board for our updates.

Reason: Still haven't found the perfect design.

Hi designers,

We will make a decision Monday and let you know. Thanks for your submissions!

Industry/Entity Type

Business

Font styles to use
Sans Serif

Colors
33b7a4
f78f20
ffffff

Requirements
Must have
• Please use our current color scheme, fonts, and logo. Attached is our logo and style guidelines. Not included in those style guidelines is the orange we also incorporate into our designs, which is #ff9a00.

Also have a look at http://www.crestwayhire.com.au, http://www.crestwayhire.com.au/blog, and http://www.linkvora.com/crestwayhirerecruitment. We want to take our current look and just modernize it a bit.

```html
<!DOCTYPE html>
<html lang="en">
<head>
<meta charset="utf-8">
<title>crestwayhire – Recruitment</title>
<link rel="stylesheet" href="https://fonts.googleapis.com/css2?family=Source+Sans+3:wght@300;400;600&display=swap">
<style>
:root{
  --teal:#33b7a4;
  --teal-dark:#1f8f8a;
  --orange:#f78f20;
  --orange-btn:#ff9a00;
  --white:#ffffff;
  --ink:#333333;
  --grey:#777777;
  --panel:#3d3d3d;
  --field:#474747;
  --badge:#ececec;
}
*{margin:0;padding:0;box-sizing:border-box}
html,body{width:1052px;height:1200px;overflow:hidden}
body{font-family:"Source Sans 3",sans-serif;color:var(--ink);background:var(--white);position:relative}
.hero{position:absolute;left:0;top:0;width:1052px;height:468px;
  background:linear-gradient(160deg,#ffffff 0%,#e9f6f5 22%,#bfe5e2 45%,#8fd3cf 65%,#66c5c2 100%)}
.logo{position:absolute;left:108px;top:34px;font-size:38px;font-weight:300;color:var(--teal);letter-spacing:-.5px;display:flex;align-items:center;gap:8px}
.logo .mark{width:18px;height:18px;border-radius:50%;background:var(--teal)}
.social{position:absolute;left:849px;top:16px;display:flex;gap:4px}
.social span{width:30px;height:30px;border-radius:5px;background:#4f86c6}
.contact{position:absolute;right:106px;top:56px;text-align:right;font-size:13px;font-weight:300;color:var(--teal-dark);line-height:23px}
.nav{position:absolute;left:105px;top:103px;width:842px;height:56px;background:var(--teal);display:flex;align-items:center;padding-left:38px;gap:48px}
.nav a{color:var(--white);font-size:18px;font-weight:600;text-decoration:none}
.tagline{position:absolute;left:140px;top:190px;width:772px;text-align:center;font-size:19px;font-weight:300;color:#6b6b6b;line-height:26px}
.finder{position:absolute;left:112px;top:272px;width:516px;height:145px;background:var(--panel);border:1px solid #222;border-radius:3px;padding:6px 32px}
.finder h2{font-size:27px;font-weight:300;color:var(--teal);line-height:32px}
.finder .cols{display:flex;gap:24px;margin-top:2px}
.finder .col{width:218px}
.finder label{display:block;color:var(--white);font-size:17px;font-weight:300;margin-bottom:3px;line-height:22px}
.finder .field{height:28px;background:var(--field);border:1px solid #555}
.finder .btn{display:inline-block;margin-top:10px;background:var(--orange-btn);color:var(--white);font-size:13px;line-height:18px;padding:2px 15px;border:1px solid #e08500}
.portal{position:absolute;left:707px;top:273px;width:235px;height:65px;background:var(--teal);color:var(--white);font-size:27px;font-weight:300;display:flex;align-items:center;justify-content:center}
.partner{position:absolute;left:707px;top:348px;width:235px;height:67px;background:var(--white);border:1px solid #ccc;display:flex;align-items:center;justify-content:center;gap:8px;font-size:30px;color:var(--teal-dark)}
.partner .mark{width:14px;height:14px;background:#888}
.dots{position:absolute;left:501px;top:441px;display:flex;gap:3px}
.dots span{width:10px;height:10px;border-radius:50%;background:#e8f4f4}
.dots span:first-child{background:var(--orange)}
.band{position:absolute;left:0;top:468px;width:1052px;height:629px;background:var(--orange)}
.content{position:absolute;left:112px;top:466px;width:828px;height:600px;background:var(--white)}
.content h3{position:absolute;left:32px;top:16px;font-size:24px;font-weight:300;color:var(--teal)}
.rule{position:absolute;left:32px;top:55px;width:762px;border-top:1px solid #ddd}
.specs{position:absolute;left:33px;top:68px;display:flex}
.specs ul{list-style:none;font-size:13.5px;line-height:26.3px}
.specs ul:nth-child(1){width:245px}
.specs ul:nth-child(2){width:280px}
.awards-title{position:absolute;left:0;width:828px;top:400px;text-align:center;font-size:24px;font-weight:300;color:var(--teal)}
.awards{position:absolute;left:68px;top:466px;display:flex;gap:28px;align-items:center}
.badge{width:88px;height:80px;background:var(--badge);border-radius:4px}
.footer{position:absolute;left:0;top:1097px;width:1052px;text-align:center}
.footer h4{font-size:14px;font-weight:400;margin-top:5px}
.footer p{font-size:11px;font-weight:300;line-height:18px;width:850px;margin:4px auto 0}
.footer small{display:block;font-size:11px;font-weight:300;color:var(--grey);margin-top:8px}
</style>
</head>
<body>
<header class="hero">
  <div class="logo"><span class="mark"></span>crestwayhire</div>
  <div class="social" aria-label="Social links"><span></span><span style="background:#5aaee0"></span><span style="background:#3b5b9e"></span></div>
  <div class="contact">Harbour CBD, Level 4, 88 Quarry Street, Sydney NSW 2000<br>Tel: 02 5550 1482 , hello@crestwayhire.com.au</div>
  <nav class="nav"><a href="#">About</a><a href="#">Clients</a><a href="#">Candidates</a><a href="#">Blog</a><a href="#">Contact Us</a></nav>
  <p class="tagline">Whether you are looking for your next career opportunity,or you are looking to recruit new people for your business.We believe in listening and tailoring our services to your needs.</p>
  <section class="finder">
    <h2>I Want to</h2>
    <div class="cols">
      <div class="col"><label>Find a job...</label><div class="field"></div><span class="btn">Search</span></div>
      <div class="col"><label>Find Employee’s</label><div class="field"></div><span class="btn">Search</span></div>
    </div>
  </section>
  <div class="portal">Talent Portal</div>
  <div class="partner"><span class="mark"></span>wagecove</div>
  <div class="dots"><span></span><span></span><span></span><span></span></div>
</header>
<div class="band"></div>
<main class="content">
  <h3>Specialities</h3>
  <div class="rule"></div>
  <div class="specs">
    <ul><li>AC Technician</li><li>» Application Engineer</li><li>» Assembler</li><li>» Automotive Engineer</li><li>» Aviation Engineer</li><li>» CEO/ MD/ Country Manager</li><li>» Chemical Engineer</li><li>» Chief Engineer</li><li>» Civil Engineer</li><li>» Consultant</li><li>» Customer Service/ Tech Support</li></ul>
    <ul><li>» Data Management/ Statistics</li><li>» Design Manager/ Engineer</li><li>» Director on Board</li><li>» Documentation/ Shipment Management</li><li>» Draughtsman</li><li>» Driver/Chauffeur</li><li>» Electrical Engineer</li><li>» Electrician</li><li>» Electronics/ Instrumentation Engineer</li><li>» Entrepreneur</li><li>» Environmental Engineer</li></ul>
    <ul><li>» Floor Supervisor</li><li>» Foreman</li><li>» Fresher</li><li>» Graduate Trainee / Management Trainee</li><li>» Industrial Engineering</li><li>» International Business Dev Mgr</li><li>» Lab Staff</li><li>» Language Expert</li><li>» Liaison</li><li>» Machine Operator</li><li>» Maintenance</li></ul>
  </div>
  <div class="awards-title">Awards</div>
  <div class="awards">
    <div class="badge" role="img" aria-label="Industry award badge"></div>
    <div class="badge" role="img" aria-label="Industry award badge"></div>
    <div class="badge" role="img" aria-label="Industry award badge"></div>
    <div class="badge" role="img" aria-label="Industry award badge"></div>
    <div class="badge" role="img" aria-label="Recruitment award badge"></div>
    <div class="badge" role="img" aria-label="Recruitment award badge"></div>
  </div>
</main>
<footer class="footer">
  <h4>Privacy Policy</h4>
  <p>At vero eos et accusamus et iusto odio dignissimos ducimus qui blanditiis praesentium voluptatum deleniti atque corrupti quos dolores et quas molestias excepturi sint occaecati cupiditate non provident, similique sunt in culpa qui officia deserunt mollitia animi, id est laborum et dolorum fuga.</p>
  <small>©2013 Company Name , All Rights Reserved</small>
</footer>
</body>
</html>
```